Caldrey Orthodontics business card

Using our existing logo (created with PixelGuild), please create a tasteful, contemporary business card. We are father and daughter orthodontists specializing in braces, clearvora, etc to design healthy, beautiful smiles for children, adolescents, and adults. We would like the design to be family-friendly but not childish.
The final design should include all of the information without looking cluttered (I hope! If necessary to achieve an optimal design, please consider making the card double-sided)
Purple, black, silver on a white card
Please include the following information:
Caldrey Orthodontics (logo)
Marisol T. Caldrey, DMD
Gordon L. Caldrey, DMD

312 Hollowmere Road
Brinlow Falls, ST 00412
555.214.3096

748C Brackenford Lane
Tarrowby, ST 00419
555.407.1582

email frontdesk@caldreyortho-example.com
website www.caldreyortho-example.com

```html
<!DOCTYPE html>
<html lang="en">
<head>
<meta charset="utf-8">
<title>Caldrey Orthodontics – Business Card</title>
<link rel="stylesheet" href="https://fonts.googleapis.com/css2?family=Cinzel:wght@400;600&family=Open+Sans:wght@400&display=swap">
<style>
  :root {
    --purple: #662d91;
    --ink: #4a4a4a;
    --silver: #8a8a8a;
    --paper: #ffffff;
    --backdrop: #d2d2d2;
  }
  * { box-sizing: border-box; margin: 0; padding: 0; }
  html, body { width: 1200px; height: 900px; overflow: hidden; }
  body {
    background: var(--backdrop);
    position: relative;
    font-family: "Open Sans", Arial, sans-serif;
  }
  .card {
    position: absolute;
    left: 250px;
    width: 700px;
    height: 400px;
    border-radius: 34px;
    overflow: hidden;
    box-shadow: 0 6px 14px rgba(0,0,0,0.25);
  }
  .card--front { top: 40px; background: var(--purple); }
  .card--back { top: 460px; background: var(--paper); }

  .brand {
    position: absolute;
    display: flex;
    align-items: center;
    gap: 18px;
    font-family: "Cinzel", Georgia, serif;
    font-weight: 600;
  }
  .brand__dot { border-radius: 50%; flex: none; }
  .brand__words { display: flex; flex-direction: column; line-height: 1; }
  .brand__name { letter-spacing: 1px; }
  .brand__sub { letter-spacing: 0.55em; }

  .card--front .brand { left: 110px; top: 150px; color: var(--paper); }
  .card--front .brand__dot { width: 60px; height: 60px; background: var(--paper); }
  .card--front .brand__name { font-size: 62px; }
  .card--front .brand__sub { font-size: 22px; margin-top: 8px; }

  .card--back .brand { left: 60px; top: 56px; color: var(--purple); }
  .card--back .brand__dot { width: 38px; height: 38px; background: var(--purple); }
  .card--back .brand__name { font-size: 38px; }
  .card--back .brand__sub { font-size: 13px; margin-top: 5px; }

  .locations {
    position: absolute;
    right: 50px;
    top: 60px;
    text-align: right;
    font-size: 16px;
    line-height: 1.35;
    color: var(--ink);
  }
  .location + .location { margin-top: 18px; }
  .location__phone { color: var(--purple); }

  .edge-mark {
    position: absolute;
    left: 0;
    top: 246px;
    width: 22px;
    height: 50px;
    background: var(--purple);
  }
  .doctors {
    position: absolute;
    left: 60px;
    top: 232px;
    font-family: "Cinzel", Georgia, serif;
    font-size: 22px;
    line-height: 1.3;
    color: var(--purple);
    font-weight: 600;
  }
  .doctors__title { color: var(--silver); font-weight: 400; }

  .contact {
    position: absolute;
    left: 60px;
    top: 310px;
    list-style: none;
    font-size: 18px;
    line-height: 1.55;
    color: var(--ink);
  }
  .contact__item { display: flex; align-items: center; gap: 10px; }
  .contact__icon { width: 16px; height: 16px; flex: none; }
  .contact__accent { color: var(--purple); }
</style>
</head>
<body>

  <section class="card card--front" aria-label="Card front">
    <div class="brand">
      <span class="brand__dot"></span>
      <span class="brand__words">
        <span class="brand__name">CALDREY</span>
        <span class="brand__sub">ORTHODONTICS</span>
      </span>
    </div>
  </section>

  <section class="card card--back" aria-label="Card back">
    <div class="brand">
      <span class="brand__dot"></span>
      <span class="brand__words">
        <span class="brand__name">CALDREY</span>
        <span class="brand__sub">ORTHODONTICS</span>
      </span>
    </div>

    <div class="locations">
      <p class="location">
        312 Hollowmere Road<br>
        Brinlow Falls, ST 00412<br>
        <span class="location__phone">555.214.3096</span>
      </p>
      <p class="location">
        748C Brackenford Lane<br>
        Tarrowby, ST 00419<br>
        <span class="location__phone">555.407.1582</span>
      </p>
    </div>

    <span class="edge-mark"></span>

    <div class="doctors">
      <p>MARISOL T. CALDREY<span class="doctors__title">, DMD</span></p>
      <p>GORDON L. CALDREY<span class="doctors__title">, DMD</span></p>
    </div>

    <ul class="contact">
      <li class="contact__item">
        <svg class="contact__icon" viewBox="0 0 16 16" aria-hidden="true">
          <rect x="1" y="3" width="14" height="10" fill="#662d91"/>
          <path d="M1 3 L8 9 L15 3" fill="none" stroke="#fff" stroke-width="1.4"/>
        </svg>
        <span>frontdesk@caldreyortho-example.com</span>
      </li>
      <li class="contact__item">
        <svg class="contact__icon" viewBox="0 0 16 16" aria-hidden="true">
          <circle cx="8" cy="8" r="7" fill="#662d91"/>
          <g fill="none" stroke="#fff" stroke-width="1">
            <ellipse cx="8" cy="8" rx="3" ry="7"/>
            <line x1="1" y1="8" x2="15" y2="8"/>
            <line x1="2.5" y1="4.5" x2="13.5" y2="4.5"/>
            <line x1="2.5" y1="11.5" x2="13.5" y2="11.5"/>
          </g>
        </svg>
        <span>www.<span class="contact__accent">caldreyortho-example.com</span></span>
      </li>
    </ul>
  </section>

</body>
</html>
```